Beautiful e-comm site for 'roadside farmers stand' online!

Need a logo design and basic e-comm website (super super simple) for new business called Brambletoft. Brambletoft is an online farmers stand where local artisans can sell 'brambletoft' goods directly from their makers!

Looking for something simple, whimsicle and clean! (Ideally with a light grey or perrywinkle and some color mixed in - word 'Brambletoft' in black - can work the pear shape in somewhere but not required!)

Target Market(s)

Hobby shoppers and 'quilo' goers who want a focus on edible things and care about ingredients!

Industry/Entity Type

E-Commerce

Number of Pages Required

2 page

Font styles to use
Decorative
Script

Colors
f3f1f8
ec1f27
cadf82

Requirements
Must have
• - Basic logo
• - Homepage
• - Product Detail Page
• - Be in a responsive, woocommerce or shopify, wordpress theme (will purchase theme after design is approved)
Nice to have
• - Matching check out & cart pages
• - 'About Us' page
• - SEO plugin
Should not have
• A cluttered look/feel.

```html
<!DOCTYPE html>
<html lang="en">
<head>
<meta charset="utf-8">
<title>Brambletoft – Home Made Goods</title>
<link href="https://fonts.googleapis.com/css2?family=Montserrat:ital,wght@0,300;0,400;0,500;0,600;0,700;1,400&display=swap" rel="stylesheet">
<style>
:root{
  --red:#c4202a;
  --red-dark:#a8161e;
  --green:#cbdf80;
  --green-soft:#d6e6a0;
  --grey-bg:#ebebeb;
  --ink:#1a1a1a;
  --text:#2b2b2b;
  --line:#9a9a9a;
  --tan:#c8a36c;
  --white:#ffffff;
}
*{box-sizing:border-box;margin:0;padding:0}
html,body{width:1200px;height:2812px;overflow:hidden}
body{position:relative;background:var(--grey-bg);font-family:"Montserrat",Arial,sans-serif;color:var(--text)}
.abs{position:absolute}

/* hero */
.hero-photo{left:0;top:0;width:1200px;height:643px;
  background:radial-gradient(circle at 20% 30%,#e8c23a 0 8%,transparent 20%),
             radial-gradient(circle at 75% 25%,#7fae3a 0 8%,transparent 22%),
             radial-gradient(circle at 30% 70%,#c7253a 0 10%,transparent 24%),
             radial-gradient(circle at 88% 60%,#f4f0e6 0 9%,transparent 20%),
             radial-gradient(circle at 55% 85%,#6c4a8a 0 8%,transparent 22%),
             linear-gradient(135deg,#b4473d,#8d2a3a 45%,#c2653a)}
.hero-shade{left:0;top:0;width:1200px;height:643px;background:rgba(40,10,20,.28)}
.header{left:0;top:0;width:1200px;height:90px;background:rgba(214,228,240,.88)}
.logo{left:122px;top:22px;font-size:38px;font-weight:600;color:var(--ink);letter-spacing:.5px}
.nav{top:36px;font-size:17px;font-weight:500;color:var(--ink);letter-spacing:.3px}
.nav-dot{left:493px;top:-10px;width:20px;height:20px;border-radius:50%;background:var(--red)}
.cart{left:1020px;top:18px;width:64px;height:50px;background:var(--red);border-radius:3px;color:var(--white);text-align:center;font-size:12px;font-weight:500}
.cart svg{display:block;margin:8px auto 1px}
.cart-badge{left:1052px;top:20px;width:18px;height:18px;border-radius:50%;background:var(--green);color:var(--ink);font-size:11px;font-weight:700;text-align:center;line-height:18px}
.hero-title{left:0;top:278px;width:1200px;text-align:center;color:var(--white);font-size:37px;font-weight:600;line-height:42px;letter-spacing:.5px}
.hero-btn{left:488px;top:388px;width:224px;height:47px;background:var(--green);border-radius:3px;font-size:20px;font-weight:600;text-align:center;line-height:47px;color:var(--ink);letter-spacing:.5px}

/* section titles */
.sec-title{left:0;width:1200px;text-align:center;font-size:32px;font-weight:300}
.rule{height:1px}
.rule::before,.rule::after{content:"";position:absolute;top:-4px;width:7px;height:7px;border:1px solid currentColor;border-radius:50%;background:inherit}
.rule.l::before{left:-7px}.rule.r::after{right:-7px}
.red-rule{background:var(--red);color:var(--red)}
.dark-rule{background:#333;color:#333}

/* cards */
.card{top:834px;width:225px;height:242px;background:var(--white);border:1px solid var(--red);border-radius:4px;overflow:hidden}
.card-photo{left:0;top:0;width:223px;height:135px}
.card-name{left:0;top:155px;width:223px;text-align:center;font-size:16px;font-weight:500;color:var(--ink)}
.price{left:81px;top:195px;width:60px;height:45px}
.price span{position:absolute;left:0;top:14px;width:60px;text-align:center;color:var(--white);font-size:16px;font-weight:700}
.card.active{background:var(--green-soft);border-color:#9aa66a;box-shadow:0 3px 8px rgba(0,0,0,.25)}
.card.active .card-photo::after{content:"";position:absolute;inset:0;background:rgba(190,218,110,.65)}
.card.active .card-name{color:#8c9a62}
.add-cart{left:44px;top:88px;width:137px;height:64px;background:#111;color:var(--white);font-size:14px;font-weight:600;text-align:center;letter-spacing:.5px}
.add-cart svg{display:block;margin:8px auto 4px}

.more-btn{left:497px;top:1146px;width:206px;height:47px;border:1px solid var(--red);border-radius:4px;color:var(--red-dark);font-size:15px;font-weight:600;text-align:center;line-height:45px;letter-spacing:.3px}

/* who we are */
.green-band{left:0;top:1232px;width:1200px;height:664px;background:var(--green);clip-path:polygon(0 71px,1200px 0,1200px 664px,0 664px)}
.about-text{top:1466px;width:345px;font-size:15px;line-height:18.6px;color:var(--ink)}
.about-text.left{left:227px;text-align:right}
.about-text.right{left:638px}
.divider-v{left:600px;top:1434px;width:1px;height:381px;background:#8fa05a}
.divider-h{top:1624px;height:1px;background:#9fb068}
.icon{top:1700px}

/* signup */
.signup-photo{left:0;top:1894px;width:1200px;height:440px;background:radial-gradient(circle at 30% 45%,#f3c4b8 0,transparent 35%),radial-gradient(circle at 75% 30%,#f1d2c6 0,transparent 35%),linear-gradient(180deg,#f7eeea,#f4e6df 60%,#f7ecea)}
.signup-veil{left:0;top:1894px;width:1200px;height:440px;background:rgba(255,255,255,.55)}
.signup-text{left:200px;top:2085px;width:800px;text-align:center;font-size:15px;line-height:19px;color:var(--ink)}
.email{left:386px;top:2162px;width:285px;height:45px;border:1px solid var(--red);background:var(--white);font-size:15px;font-style:italic;color:#444;padding:12px 0 0 12px}
.subscribe{left:686px;top:2162px;width:130px;height:45px;background:var(--red);color:var(--white);font-size:15px;font-weight:700;text-align:center;line-height:45px}

/* footer */
.footer{left:0;top:2334px;width:1200px;height:478px;background:var(--grey-bg)}
.foot-panel{left:118px;top:2423px;width:388px;height:305px}
.foot-logo{left:140px;top:2463px;font-size:34px;font-weight:600;color:var(--white)}
.foot-about{left:139px;top:2525px;width:340px;font-size:13.5px;line-height:17.5px;color:var(--white)}
.social{top:2615px;width:30px;height:30px;background:var(--white);border-radius:2px}
.foot-head{top:2486px;font-size:14px;font-weight:600;color:var(--red)}
.foot-list{list-style:none;top:2512px;font-size:13.5px;line-height:26px;color:var(--ink)}
.foot-list li::before{content:"• "}
.foot-rule{left:531px;top:2608px;width:547px;height:1px;background:#b8b8b8}
.copy{top:2636px;font-size:13.5px;color:var(--ink)}
</style>
</head>
<body>

<!-- hero -->
<div class="abs hero-photo" role="img" aria-label="Close-up photograph of colourful home made candies and sprinkles"></div>
<div class="abs hero-shade"></div>
<header class="abs header"></header>
<div class="abs nav-dot"></div>
<div class="abs logo">Brambletoft</div>
<nav>
  <div class="abs nav" style="left:480px">HOME</div>
  <div class="abs nav" style="left:557px">PRODUCT</div>
  <div class="abs nav" style="left:669px">STORES</div>
  <div class="abs nav" style="left:759px">WHO WE ARE</div>
  <div class="abs nav" style="left:900px">CONTACT</div>
</nav>
<div class="abs cart">
  <svg width="22" height="18" viewBox="0 0 22 18" fill="none" stroke="#fff" stroke-width="2"><path d="M1 2h3l3 10h11l3-7H6"/><circle cx="9" cy="16" r="1.5" fill="#fff"/><circle cx="16" cy="16" r="1.5" fill="#fff"/></svg>
  CART
</div>
<div class="abs cart-badge">2</div>
<h1 class="abs hero-title">EXPLORE HOME MADE ITEMS<br>FEEL THE TOUCH OF LOVE</h1>
<div class="abs hero-btn">BROWS PRODUCTS</div>

<!-- featured -->
<div class="abs rule red-rule l" style="left:276px;top:709px;width:174px;background:var(--red)"></div>
<div class="abs rule red-rule r" style="left:750px;top:709px;width:174px;background:var(--red)"></div>
<h2 class="abs sec-title" style="top:686px;color:var(--red)">Featured Products</h2>
<p class="abs" style="left:0;top:742px;width:1200px;text-align:center;font-size:15px;color:var(--ink)">Anything that is easily made at home by people who like crafts.</p>

<div class="abs card active" style="left:118px">
  <div class="abs card-photo" role="img" aria-label="Photo of cherry fruit jam jars" style="background:linear-gradient(135deg,#8aa857,#b8c98a 50%,#7e9a4c)"></div>
  <div class="abs card-name">Cherry Fruit Jams</div>
  <svg class="abs price" viewBox="0 0 60 45"><polygon points="0,0 30,9 60,0 60,45 0,45" fill="var(--tan)"/></svg>
  <div class="abs price"><span>$10</span></div>
  <div class="abs add-cart">
    <svg width="22" height="18" viewBox="0 0 22 18" fill="none" stroke="#fff" stroke-width="2"><path d="M1 2h3l3 10h11l3-7H6"/><circle cx="9" cy="16" r="1.5" fill="#fff"/><circle cx="16" cy="16" r="1.5" fill="#fff"/></svg>
    ADD TO CART
  </div>
</div>
<div class="abs card" style="left:364px">
  <div class="abs card-photo" role="img" aria-label="Photo of a jar of mixed vegetable pickle" style="background:linear-gradient(135deg,#a89a7a,#d9c79a 45%,#c4632f 70%,#6e8a3a)"></div>
  <div class="abs card-name">Mix Vegetable Pickle</div>
  <svg class="abs price" viewBox="0 0 60 45"><polygon points="0,0 30,9 60,0 60,45 0,45" fill="var(--red)"/></svg>
  <div class="abs price"><span>$11</span></div>
</div>
<div class="abs card" style="left:611px">
  <div class="abs card-photo" role="img" aria-label="Photo of a stack of fresh cookies" style="background:linear-gradient(180deg,#1c1c22,#2a2a30 45%,#b07a3a 70%,#d9d3c6)"></div>
  <div class="abs card-name">Fresh Cookies</div>
  <svg class="abs price" viewBox="0 0 60 45"><polygon points="0,0 30,9 60,0 60,45 0,45" fill="var(--red)"/></svg>
  <div class="abs price"><span>$08</span></div>
</div>
<div class="abs card" style="left:857px">
  <div class="abs card-photo" role="img" aria-label="Photo of a bowl of colourful jelly beans" style="background:radial-gradient(circle at 50% 50%,#e2a53a 0,#c43a3a 25%,#5a9a3a 45%,#eceae6 62%,#bdbdbd)"></div>
  <div class="abs card-name">Colourfull Jelly Beens</div>
  <svg class="abs price" viewBox="0 0 60 45"><polygon points="0,0 30,9 60,0 60,45 0,45" fill="var(--red)"/></svg>
  <div class="abs price"><span>$14</span></div>
</div>

<div class="abs" role="img" aria-label="Strawberry" style="left:22px;top:1128px;width:100px;height:112px;border-radius:45% 45% 50% 50%;background:radial-gradient(circle at 40% 55%,#e8352e,#b7161b)"></div>
<div class="abs" role="img" aria-label="Pair of cherries" style="left:919px;top:1170px;width:84px;height:48px;border-radius:40px;background:radial-gradient(circle at 30% 50%,#8a1424,#4e0a14 70%)"></div>
<div class="abs more-btn">MORE PRODUCTS</div>

<!-- who we are -->
<div class="abs green-band"></div>
<div class="abs" role="img" aria-label="Plate of jam filled crumble bars with fresh mint" style="left:881px;top:1262px;width:319px;height:162px;border-radius:50% 45% 40% 50%;background:radial-gradient(ellipse at 65% 45%,#d19a44 0,#b65c3a 30%,#4e8a2e 55%,transparent 72%)"></div>
<div class="abs rule dark-rule l" style="left:309px;top:1373px;width:175px"></div>
<div class="abs rule dark-rule r" style="left:718px;top:1373px;width:175px"></div>
<h2 class="abs sec-title" style="top:1350px;color:var(--ink)">Who We Are</h2>

<p class="abs about-text left">Donec dictum sollicitudin luctus. Donec est erat, placerat non nisi sit amet, pharetra auctor ligula. Donec a lectus nibh. Morbi pretium maximus risus, eget pretium turpis. Aliquam lectus ex, volutpat quis ullamcorper at, blandit a eros. Curabitur id nulla vitae lectus faucibus consectetur ac at sem. Donec et elit quis augue porta eleifend.</p>
<p class="abs about-text right">Donec dictum sollicitudin luctus. Donec est erat, placerat non nisi sit amet, pharetra auctor ligula. Donec a lectus nibh. Morbi pretium maximus risus, eget pretium turpis. Aliquam lectus ex, volutpat quis ullamcorper at, blandit a eros. Curabitur id nulla vitae lectus faucibus consectetur ac at sem. Donec et elit quis augue porta eleifend.</p>
<div class="abs divider-v"></div>
<div class="abs divider-h" style="left:203px;width:382px"></div>
<div class="abs divider-h" style="left:615px;width:381px"></div>

<svg class="abs icon" style="left:294px" width="70" height="88" viewBox="0 0 70 88" fill="none" stroke="#6f7a50" stroke-width="2.5"><rect x="14" y="4" width="42" height="12" rx="3"/><path d="M10 22q0-6 8-6h34q8 0 8 6v56q0 6-6 6H16q-6 0-6-6z"/><circle cx="26" cy="46" r="6"/><circle cx="44" cy="52" r="6"/><circle cx="32" cy="66" r="6"/></svg>
<svg class="abs icon" style="left:395px" width="70" height="88" viewBox="0 0 70 88" fill="none" stroke="#6f7a50" stroke-width="2.5"><rect x="12" y="4" width="46" height="12" rx="3"/><path d="M6 24q0-8 10-8h38q10 0 10 8v52q0 8-8 8H14q-8 0-8-8z"/><circle cx="24" cy="42" r="4"/><circle cx="42" cy="48" r="5"/><circle cx="28" cy="64" r="5"/><circle cx="48" cy="68" r="3"/></svg>
<svg class="abs icon" style="left:502px" width="72" height="88" viewBox="0 0 72 88" fill="none" stroke="#6f7a50" stroke-width="2.5"><rect x="8" y="4" width="56" height="12" rx="3"/><rect x="4" y="16" width="64" height="68" rx="6"/><path d="M14 34l16 14M30 26l18 30M44 36l14 16M20 60l18 14"/></svg>
<svg class="abs icon" style="left:636px" width="90" height="88" viewBox="0 0 90 88" fill="none" stroke="#6f7a50" stroke-width="2.5"><path d="M6 80q-4-14 10-16q2-12 16-8q8-4 14 4v20z"/><rect x="46" y="36" width="34" height="48" rx="5"/><path d="M56 36V24h14v12M63 24V12h12"/><rect x="52" y="50" width="22" height="18"/></svg>
<svg class="abs icon" style="left:765px" width="58" height="88" viewBox="0 0 58 88" fill="none" stroke="#6f7a50" stroke-width="2.5"><path d="M22 4h14v16q18 10 16 34q-2 24-14 30H20Q8 78 6 54Q4 30 22 20z"/><path d="M10 44h38M8 58h42M12 70h34"/></svg>
<svg class="abs icon" style="left:862px" width="100" height="88" viewBox="0 0 100 88" fill="none" stroke="#6f7a50" stroke-width="2.5"><rect x="8" y="20" width="84" height="48"/><rect x="14" y="26" width="72" height="36"/><path d="M50 30l18 14-18 14-18-14z"/><path d="M8 20l-6-6M92 20l6-6M8 68l-6 6M92 68l6 6"/></svg>

<div class="abs" role="img" aria-label="Mason jar filled with strawberries and water" style="left:75px;top:1669px;width:178px;height:206px;border-radius:16px 16px 28px 28px;background:linear-gradient(180deg,#e23a3a 0 14%,#f2e8e6 14% 20%,#f0c6c4 20%,#e15458 60%,#c9cfc4)"></div>
<div class="abs" role="img" aria-label="Sliced strawberries with mint leaves" style="left:19px;top:1866px;width:206px;height:94px;border-radius:50%;background:radial-gradient(ellipse at 40% 50%,#d42a2e 0,#b81c22 35%,#4e8a32 60%,transparent 72%)"></div>

<!-- signup -->
<div class="abs signup-photo" role="img" aria-label="Soft background photo of glass jars of home made jam"></div>
<div class="abs signup-veil"></div>
<div class="abs rule dark-rule l" style="left:219px;top:2040px;width:81px"></div>
<div class="abs rule dark-rule r" style="left:904px;top:2040px;width:80px"></div>
<h2 class="abs sec-title" style="top:2017px;color:var(--ink)">Sign up for Special Offers and Stories</h2>
<p class="abs signup-text">Suspendisse odio quam, mollis id semper non, finibus sit amet nulla. Vivamus malesuada est eu tristique sodales. Morbi a sem odio.</p>
<div class="abs email">Enter your Email ID</div>
<div class="abs subscribe">SUBSCRIBE</div>

<!-- footer -->
<footer class="abs footer"></footer>
<svg class="abs foot-panel" viewBox="0 0 388 305"><polygon points="0,0 388,0 388,305 194,277 0,305" fill="var(--red)"/></svg>
<div class="abs foot-logo">Brambletoft</div>
<p class="abs foot-about">Curabitur id magna urna. Duis non interdum sem. Phasellus egestas libero vitae commodo consequat. Aliquam nec aliquet neque, sed tempus dui.</p>
<div class="abs social" style="left:139px" aria-label="Social link"></div>
<div class="abs social" style="left:176px" aria-label="Social link"></div>
<div class="abs social" style="left:214px" aria-label="Social link"></div>
<div class="abs social" style="left:253px" aria-label="Social link"></div>

<div class="abs foot-head" style="left:568px">CUSTOMER SERVICE</div>
<ul class="abs foot-list" style="left:568px"><li>Contact Us</li><li>Returns</li><li>Site Map</li></ul>
<div class="abs foot-head" style="left:861px">INFORMATION</div>
<ul class="abs foot-list" style="left:861px"><li>Delivery Information</li><li>Privacy Policy</li><li>Terms &amp; Conditions</li></ul>
<div class="abs foot-rule"></div>
<div class="abs copy" style="left:566px">© 2018 Brambletoft. All Rights Reserved.</div>
<div class="abs copy" style="left:983px">Privacy Policy</div>

</body>
</html>
```